Vel

I have the logo for the back already. Need the front to match.
Need a VEL logo which I can provide or you can download one - VEL Realty in canada... Back of the card will be my logo and name. Front will have the info...
I would like a black background. Match colors on front to the back..
Details on Card

Target Market(s)

Realestate clients.. Keep it classy like the logo

Contact Information for Business Card

Reena Dhot office - 4035550187 cell - 4035550264 email - Reena@ReenaDhot.Com. website - ReenaDhot.Com Facebook - RDhotRealty Instagram - Reena_Yyc_Realtor Address - 514 - 23 St NE | T3K5M8

Colors
3176b5
33a6d7
85cae6

Requirements
Must have
• same color scheme as the logo
logo will be on the back
Black Background
Horizontal card
The one side of the card should be clean. like I stated, just my logo " Reena Dhot " and nothing else

```html
<!DOCTYPE html>
<html lang="en">
<head>
<meta charset="utf-8">
<title>Reena Dhot – Business Card</title>
<link href="https://fonts.googleapis.com/css2?family=Cinzel:wght@600&family=Arimo:wght@400&display=swap" rel="stylesheet">
<style>
  :root {
    --backdrop: #a4a4a4;
    --card: #0d0d0d;
    --brand-blue: #3176b5;
    --icon-blue: #33a6d7;
    --ink: #d6d6d6;
    --badge: #3a3a3a;
    --edge: #2a2a2a;
  }
  * { margin: 0; padding: 0; box-sizing: border-box; }
  html, body { width: 1200px; height: 848px; overflow: hidden; }
  body {
    background: var(--backdrop);
    position: relative;
    font-family: "Arimo", Arial, sans-serif;
  }
  .card {
    position: absolute;
    top: 276px;
    width: 525px;
    height: 300px;
    background: var(--card);
    border: 1px solid var(--edge);
  }
  .card--info { left: 50px; }
  .card--logo { left: 625px; }

  /* Contact side */
  .info__name {
    position: absolute;
    left: 36px;
    top: 34px;
    font-family: "Cinzel", Georgia, serif;
    font-weight: 600;
    font-size: 22px;
    letter-spacing: 1px;
    color: var(--brand-blue);
  }
  .contact {
    position: absolute;
    right: 30px;
    bottom: 36px;
    list-style: none;
  }
  .contact__item {
    display: flex;
    justify-content: flex-end;
    align-items: center;
    gap: 8px;
    font-size: 13px;
    line-height: 19px;
    color: var(--ink);
  }
  .contact__icon { width: 11px; height: 11px; flex: none; }

  /* Logo side */
  .logo__name {
    position: absolute;
    left: 0; right: 0;
    top: 92px;
    text-align: center;
    font-family: "Cinzel", Georgia, serif;
    font-weight: 600;
    font-size: 44px;
    letter-spacing: 2px;
    color: var(--brand-blue);
  }
  .affiliations {
    position: absolute;
    left: 0; right: 0;
    top: 186px;
    display: flex;
    justify-content: center;
    align-items: center;
    gap: 22px;
  }
  .affiliation-badge {
    width: 62px;
    height: 30px;
    background: var(--badge);
    border-radius: 3px;
  }
  .brokerage {
    font-family: "Arimo", Arial, sans-serif;
    font-weight: 400;
    font-size: 13px;
    color: var(--ink);
  }
</style>
</head>
<body>

<section class="card card--info" aria-label="Contact side">
  <h1 class="info__name">REENA DHOT</h1>
  <ul class="contact">
    <li class="contact__item">4035550187
      <svg class="contact__icon" viewBox="0 0 12 12"><path fill="var(--icon-blue)" d="M2.5 1l2 2.2-1 1.3c.7 1.5 1.8 2.6 3.3 3.3l1.3-1 2.2 2-1.2 1.7C5.2 10.3 1.7 6.8 1 2.2z"/></svg>
    </li>
    <li class="contact__item">4035550264
      <svg class="contact__icon" viewBox="0 0 12 12"><rect x="3" y="0.8" width="6" height="10.4" rx="1" fill="none" stroke="var(--icon-blue)" stroke-width="1.3"/></svg>
    </li>
    <li class="contact__item">Reena@ReenaDhot.Com
      <svg class="contact__icon" viewBox="0 0 12 12"><rect x="0.5" y="2.5" width="11" height="7" fill="var(--icon-blue)"/><path d="M0.8 3l5.2 3.6L11.2 3" fill="none" stroke="var(--card)" stroke-width="0.9"/></svg>
    </li>
    <li class="contact__item">ReenaDhot.Com
      <svg class="contact__icon" viewBox="0 0 12 12"><circle cx="6" cy="6" r="5" fill="none" stroke="var(--icon-blue)" stroke-width="1.4"/><path d="M1 6h10M6 1v10" stroke="var(--icon-blue)" stroke-width="1"/></svg>
    </li>
    <li class="contact__item">RDhotRealty
      <svg class="contact__icon" viewBox="0 0 12 12"><circle cx="6" cy="6" r="5" fill="var(--icon-blue)"/></svg>
    </li>
    <li class="contact__item">Reena_Yyc_Realtor
      <svg class="contact__icon" viewBox="0 0 12 12"><circle cx="6" cy="6" r="5" fill="var(--icon-blue)"/></svg>
    </li>
    <li class="contact__item">514 - 23 St NE T3K5M8
      <svg class="contact__icon" viewBox="0 0 12 12"><path fill="var(--icon-blue)" d="M6 0.5a4 4 0 0 1 4 4c0 3-4 7-4 7s-4-4-4-7a4 4 0 0 1 4-4z"/><circle cx="6" cy="4.5" r="1.5" fill="var(--card)"/></svg>
    </li>
  </ul>
</section>

<section class="card card--logo" aria-label="Logo side">
  <h2 class="logo__name">REENA DHOT</h2>
  <div class="affiliations">
    <div class="affiliation-badge" role="img" aria-label="Partner network badge"></div>
    <div class="affiliation-badge" role="img" aria-label="Luxury listing network badge"></div>
    <span class="brokerage">VEL Realty</span>
  </div>
</section>

</body>
</html>
```